Dune Loop needs some awesome stationary

Do you have what it takes to get my brand? You either do or you don't, have a crack at a design and you my just win my business.

I don't want to waste your or my time, so put your creative genius on either a business card or envelope.

I however need a package of stationary that follows the same brand. I will message you to complete the remaining should I like your first submission.

Here is what I need, have a go!

Basically I need the following for my small business based in melbourne.
- Letterhead (printer ready and MS Word)
- Business Card
- Compliments Slip
- Envelope
- Proposal Cover Page (MS Word only)
- Presentation Folder
- Harbor Tally Cards
- Student Name Tent
- Index Cards
- Tack-Pad

I am establishing the brand and it must be modern, professional but also relaxed; that is not formal and not corporate. It represents a company are leaders, but small enough to care and operate like a bunch of friends. We are bringing people and conversations back to business, and turfing out all the bureaucracy and crazy and wasteful procedures. Its about "lets talk and figure it out together and find even better ways".

Target Market(s)

Mainly companies that build software products, but Agile practices are used in many other industries (even graphic design projects)

Industry/Entity Type

Information Technology

Font styles to use
Sans Serif

Colors
3176b5
aaaaaa

Requirements
Must have
• I like curves and circles and not boxes or rectangles.
• I want a colour rich design with my brand colours, but it must be balanced.
• I want more modern than traditional, but simple modern
Should not have
• Not corporate
• Please don't waste my time if your not going to think about it.
• Don't mess with my primary logo
• Don't change my colours
• Don't overlay logo on image

```html
<!DOCTYPE html>
<html lang="en">
<head>
<meta charset="utf-8">
<title>Dune Loop – Business Card</title>
<link href="https://fonts.googleapis.com/css2?family=Carlito:wght@400;700&display=swap" rel="stylesheet">
<style>
  :root {
    --brand-blue: #2a559a;
    --brand-grey: #8a94a1;
    --accent-grey: #aaaaaa;
    --ink: #2b2b2b;
    --card-white: #f3f3f4;
    --backdrop: #e8e8e9;
    --rule: #b9bcc2;
  }
  * { box-sizing: border-box; margin: 0; padding: 0; }
  html, body { width: 1200px; height: 800px; overflow: hidden; }
  body {
    position: relative;
    background: var(--backdrop);
    font-family: "Carlito", "Calibri", sans-serif;
    color: var(--ink);
  }
  .card {
    position: absolute;
    top: 248px;
    width: 430px;
    height: 279px;
    overflow: hidden;
  }
  .card-front { left: 112px; background: var(--card-white); }
  .card-back {
    left: 651px;
    background: linear-gradient(125deg, var(--brand-grey) 0%, var(--brand-grey) 45%, var(--brand-blue) 62%, var(--brand-blue) 100%);
  }

  .brand {
    position: absolute;
    top: 36px;
    right: 30px;
    display: flex;
    align-items: center;
    gap: 10px;
  }
  .brand-dot {
    width: 30px; height: 30px;
    border-radius: 50%;
    background: var(--brand-blue);
  }
  .brand-name {
    font-size: 38px;
    font-weight: 700;
    color: var(--brand-blue);
    line-height: 1;
  }

  .person { position: absolute; left: 22px; top: 110px; }
  .person-name { font-size: 20px; color: var(--brand-blue); line-height: 1; }
  .person-role { font-size: 11px; font-weight: 700; margin-top: 8px; }

  .divider {
    position: absolute;
    left: 12px; top: 163px;
    width: 402px; height: 1px;
    background: var(--rule);
  }
  .divider::after {
    content: "";
    position: absolute;
    left: 158px; top: -2px;
    width: 86px; height: 4px;
    background: var(--brand-blue);
  }

  .contact {
    position: absolute;
    top: 180px;
    font-size: 14px;
    line-height: 18.5px;
    list-style: none;
  }
  .contact-personal { left: 22px; }
  .contact-company { left: 260px; }
  .contact li { display: flex; align-items: flex-start; }
  .contact-icon { width: 11px; height: 13px; margin: 3px 10px 0 0; flex: none; }

  .web-arc { position: absolute; inset: 0; }
  .web-arc text {
    font-family: "Carlito", "Calibri", sans-serif;
    font-size: 14px;
    letter-spacing: 2.5px;
    fill: #ffffff;
  }
</style>
</head>
<body>
  <section class="card card-front">
    <div class="brand">
      <span class="brand-dot"></span>
      <span class="brand-name">Dune Loop</span>
    </div>

    <div class="person">
      <p class="person-name">Grant Kelso</p>
      <p class="person-role">CEO, Professional Agile Trainer</p>
    </div>

    <div class="divider"></div>

    <ul class="contact contact-personal">
      <li>
        <svg class="contact-icon" viewBox="0 0 11 13"><path d="M5.5 0.5a4 4 0 0 1 4 4c0 3-4 8-4 8s-4-5-4-8a4 4 0 0 1 4-4z" fill="#2a559a"/><circle cx="5.5" cy="4.5" r="1.5" fill="#f3f3f4"/></svg>
        <span>PO Box 4180, Ashwood Vale<br>Vale, VIC 3190, Australia</span>
      </li>
      <li>
        <svg class="contact-icon" viewBox="0 0 11 13"><circle cx="5.5" cy="6.5" r="5" fill="#2a559a"/><path d="M3 5h5v3H3z M3 5l2.5 2L8 5" fill="none" stroke="#f3f3f4" stroke-width="0.8"/></svg>
        <span>grant@dune-loop.com.au</span>
      </li>
      <li>
        <svg class="contact-icon" viewBox="0 0 11 13"><path d="M2 1.5l2 .3.8 2.6-1.3 1a6 6 0 0 0 3 3l1-1.3 2.6.8.3 2c-4.5 1-9.4-3.9-8.4-8.4z" fill="#2a559a"/></svg>
        <span>+61 400 123 987</span>
      </li>
    </ul>

    <ul class="contact contact-company">
      <li>Dune Loop Pty Ltd</li>
      <li>ABN 12 345 678 901</li>
      <li>Phone 1300LOOPS</li>
      <li>www.dune-loop.com.au</li>
    </ul>
  </section>

  <section class="card card-back" role="img" aria-label="Large flowing brand swirl in grey and blue with dark navy edges">
    <svg class="web-arc" width="430" height="279" viewBox="0 0 430 279">
      <path id="web-path" d="M330 30 A 150 150 0 0 1 375 240" fill="none"/>
      <text><textPath href="#web-path">www.dune-loop.com.au</textPath></text>
    </svg>
  </section>
</body>
</html>
```